Business card for a Exhibition booth fabrication company

Hi. My company would like to change our corporate name card. We are an events and Exhibition stand builder company. We would like our corporate name card to resonate what we do. I need someone to create something unique that relates to the industry that I am in. The graphic designer should be creative to incorporate the elements of my industry and try to blend in well in the design of the card. Our aim is to ensure that we are unique and our card can look different from our competitors.
Updates

The decision maker was very busy and didnt had time to make this decision

Target Market(s)

Marketing and events manager from all companies

Contact Information for Business Card

The business card should have the following details:
Name
Job Title
Email
Website

Colors

Designer to choose colors to be used in the design.

Requirements
Must have
• The card must be look something that is relevant to the service that I am providing. My website is: www.velmora-buildworks.example
• You can see my website to get more information on what service that I am doing
Nice to have
• On the back of my card, I would like to have a globe image with the incorporation of my company logo. This is to indicate that my services can be done in any part of the world.

```html
<!DOCTYPE html>
<html lang="en">
<head>
<meta charset="UTF-8">
<title>Velmora Buildworks – Business Card</title>
<link rel="stylesheet" href="https://fonts.googleapis.com/css2?family=Montserrat:wght@500;600;700;800&display=swap">
<style>
  :root {
    --stage: #1c1f26;
    --card-front: #000000;
    --card-back: #ffffff;
    --ink-light: #ffffff;
    --ink-grey: #6a6a6a;
    --map-grey: #ececec;
    --accent-red: #e3171e;
  }
  * { margin: 0; padding: 0; box-sizing: border-box; }
  html, body { width: 1200px; height: 800px; overflow: hidden; }
  body {
    background: var(--stage);
    font-family: 'Montserrat', Arial, sans-serif;
    position: relative;
  }
  .card {
    position: absolute;
    top: 240px;
    width: 540px;
    height: 320px;
    box-shadow: 0 12px 30px rgba(0,0,0,0.45);
    overflow: hidden;
  }
  /* Front */
  .card--front { left: 40px; background: var(--card-front); color: var(--ink-light); }
  .front__web, .front__email {
    position: absolute; left: 0; right: 0; text-align: center;
    font-size: 13px; font-weight: 600; letter-spacing: 2.6px; text-transform: uppercase;
  }
  .front__web { top: 44px; }
  .front__email { bottom: 44px; }
  .front__identity {
    position: absolute; left: 0; right: 0; top: 50%; transform: translateY(-50%);
    text-align: center;
  }
  .front__name { font-size: 34px; font-weight: 800; letter-spacing: 1px; line-height: 1; }
  .front__title { margin-top: 6px; font-size: 12.5px; font-weight: 600; letter-spacing: 3px; }
  .front__contact {
    position: absolute; top: 50%; width: 200px;
    text-align: center; font-size: 11.5px; font-weight: 600; letter-spacing: 2.4px; line-height: 1.6;
    text-transform: uppercase;
  }
  .front__contact--left { left: 40px; transform: translate(-50%, -50%) rotate(-90deg); }
  .front__contact--right { right: 40px; transform: translate(50%, -50%) rotate(90deg); }

  /* Back */
  .card--back { left: 620px; background: var(--card-back); }
  .back__map {
    position: absolute; left: 40px; top: 50px; width: 460px; height: 180px;
    border-radius: 50% 50% 8% 8% / 70% 70% 10% 10%;
    background: radial-gradient(ellipse at 50% 40%, #f3f3f3 0%, var(--map-grey) 55%, rgba(236,236,236,0) 100%);
  }
  .back__shadow {
    position: absolute; left: 60px; right: 60px; top: 250px; height: 24px;
    background: radial-gradient(ellipse at center, rgba(0,0,0,0.06), rgba(0,0,0,0) 70%);
  }
  .back__brand {
    position: absolute; left: 0; right: 0; top: 138px;
    display: flex; flex-direction: column; align-items: center; gap: 12px;
  }
  .back__mark { width: 26px; height: 26px; border-radius: 50%; background: var(--accent-red); }
  .back__name {
    font-size: 15px; font-weight: 600; letter-spacing: 2.6px; color: var(--ink-grey); text-transform: uppercase;
  }
</style>
</head>
<body>
  <section class="card card--front" aria-label="Business card front">
    <p class="front__web">www.velmora-buildworks.example</p>
    <p class="front__contact front__contact--left">Singapore Contact<br>+65 91234567</p>
    <div class="front__identity">
      <h1 class="front__name">JOHN DOE</h1>
      <p class="front__title">FABRICATION EXPERT</p>
    </div>
    <p class="front__contact front__contact--right">Qatar Contact<br>+974 70001234</p>
    <p class="front__email">john@velmora-buildworks.example</p>
  </section>

  <section class="card card--back" aria-label="Business card back">
    <div class="back__map" role="img" aria-label="Faint grey world map curving over the card"></div>
    <div class="back__shadow"></div>
    <div class="back__brand">
      <span class="back__mark"></span>
      <p class="back__name">Velmora Buildworks</p>
    </div>
  </section>
</body>
</html>
```